Exercise Physiologist needs business cards

I have a logo, I need business cards (Sole trader) as I am moving to a new location and would like an updated look. I provide gym based exercise rehabilitation, injury prevention and movement assessments. I have over 13 years experience as an Exercise Physiologist. I would like the cards to look professional but not boring and can be a little different to stand out when sitting with other Allied Health Professional cards.

Target Market(s)

GP's, Allied health practitioners, people with injuries wanting to exercise

Industry/Entity Type

Health And Wellness

Contact Information for Business Card

Megan Trowbridge - Exercise Physiologist 0487 926 350
52 Wattlebird Lane
Kellbrook North
(Door 4, Brennock Fitness)
vornalhealth@mailbox-example.com
facebook.com/Vornal

Requirements
Must have
• I would like to include a section to add next appointment date and time space to the back of the card.
Nice to have
• Rounded corners and a black background on 1 or 2 sides.
Should not have
• Pictures of fit/toned bodies etc

```html
<!DOCTYPE html>
<html lang="en">
<head>
<meta charset="utf-8">
<title>Vornal Health &amp; Rehabilitation — Business Card</title>
<link href="https://fonts.googleapis.com/css2?family=Arimo:wght@400;700&display=swap" rel="stylesheet">
<style>
  :root {
    --stage: #2b2b2d;
    --brand-blue: #1f5fc4;
    --brand-blue-dark: #164a9e;
    --ink-blue: #1a4f9c;
    --soft-blue: #4a90cf;
    --mark-fill: #5a9fd6;
    --card-white: #f4f5f7;
    --line-light: rgba(255,255,255,0.75);
  }
  * { box-sizing: border-box; margin: 0; padding: 0; }
  html, body {
    width: 1200px; height: 997px; overflow: hidden;
    background: var(--stage);
    font-family: "Arimo", Arial, sans-serif;
  }
  .stage { position: relative; width: 1200px; height: 997px; }
  .card {
    position: absolute; top: 330px; width: 540px; height: 320px;
    border-radius: 22px; overflow: hidden;
  }
  .card--back {
    left: 50px;
    background: linear-gradient(160deg, #2a6fd6 0%, var(--brand-blue) 55%, var(--brand-blue-dark) 100%);
    color: #fff;
  }
  .card--front {
    left: 610px;
    background: var(--card-white);
    border-bottom: 12px solid var(--brand-blue);
    color: var(--ink-blue);
  }
  .brand { position: absolute; left: 36px; top: 30px; display: flex; align-items: center; gap: 14px; }
  .brand__mark {
    width: 74px; height: 74px; border-radius: 50%; flex: none;
    background: var(--mark-fill); border: 5px solid var(--brand-blue);
  }
  .card--back .brand__mark { border-color: #fff; background: #7fb3e6; }
  .brand__text { display: flex; flex-direction: column; }
  .brand__name { font-size: 46px; line-height: 1; color: var(--brand-blue); }
  .card--back .brand__name { color: #fff; }
  .brand__tagline { font-size: 13px; letter-spacing: 0.5px; margin-top: 4px; color: var(--soft-blue); }
  .card--back .brand__tagline { color: #d6e6fa; }

  .appointment { position: absolute; left: 150px; right: 36px; top: 140px; }
  .appointment__field {
    font-size: 14px; letter-spacing: 1px; text-align: center;
    padding-bottom: 26px; margin-bottom: 16px;
    border-bottom: 1px dashed var(--line-light);
  }

  .contact { position: absolute; left: 126px; right: 36px; top: 116px; }
  .contact__name { font-size: 19px; font-weight: 700; letter-spacing: 0.5px; line-height: 1.2; }
  .contact__role { font-size: 15px; color: var(--soft-blue); margin-top: 2px; }
  .contact__list {
    list-style: none; margin-top: 12px; width: 280px;
    text-align: center; font-size: 14px; color: var(--soft-blue);
  }
  .contact__item { margin-bottom: 8px; line-height: 1.4; }
  .contact__item--phone { font-size: 15px; }
  .contact__icon { display: block; width: 18px; height: 18px; margin: 0 auto 5px; }
</style>
</head>
<body>
<main class="stage">

  <section class="card card--back" aria-label="Card back">
    <div class="brand">
      <span class="brand__mark"></span>
      <div class="brand__text">
        <span class="brand__name">vornal</span>
        <span class="brand__tagline">HEALTH &amp; REHABILITATION</span>
      </div>
    </div>
    <div class="appointment">
      <p class="appointment__field">NEXT APPOINTMENT</p>
      <p class="appointment__field">DATE &amp; TIME</p>
    </div>
  </section>

  <section class="card card--front" aria-label="Card front">
    <div class="brand">
      <span class="brand__mark"></span>
      <div class="brand__text">
        <span class="brand__name">vornal</span>
        <span class="brand__tagline">HEALTH &amp; REHABILITATION</span>
      </div>
    </div>
    <div class="contact">
      <p class="contact__name">MEGAN TROWBRIDGE</p>
      <p class="contact__role">Exercise Physiologist</p>
      <ul class="contact__list">
        <li class="contact__item contact__item--phone">
          <svg class="contact__icon" viewBox="0 0 18 18" aria-hidden="true">
            <rect width="18" height="18" rx="2" fill="#1a4f9c"/>
            <path d="M5 4c1 0 1.5 2 1.5 2.6 0 .6-.8.9-.8 1.4.4 1.3 2 2.9 3.3 3.3.5 0 .8-.8 1.4-.8.6 0 2.6.5 2.6 1.5 0 .9-1 1.9-2 1.9C7.5 13.9 4.1 10.5 4.1 6 4.1 5 4.3 4 5 4z" fill="#fff"/>
          </svg>
          0487 926 350
        </li>
        <li class="contact__item">
          <svg class="contact__icon" viewBox="0 0 18 18" aria-hidden="true">
            <rect width="18" height="18" rx="2" fill="#1a4f9c"/>
            <path d="M9 3.5a3.5 3.5 0 0 0-3.5 3.5C5.5 10 9 14.5 9 14.5S12.5 10 12.5 7A3.5 3.5 0 0 0 9 3.5zm0 5a1.5 1.5 0 1 1 0-3 1.5 1.5 0 0 1 0 3z" fill="#fff"/>
          </svg>
          52 Wattlebird Lane, Kellbrook North<br>(Door 4, Brennock Fitness)
        </li>
      </ul>
    </div>
  </section>

</main>
</body>
</html>
```